PEBBLEJARMAN.COM NEEDS FACELIFT!!!

Please see www.pebblejarman.com for the basics. I am a glass artist who sells to retail market (art shows and e-commerce) as well as wholsale to art galleries nation wide. My site needs to serve both types of customer. I did the basics years ago, but now it's old and outdated . I need to totally rework the site, adding functionality as well as a new look.
My criteria are:
1. Need e-commerce page (cart) that allows for the rapid uploading of new artwork for my retail market.
2. Need separate login/e-commerce page for my wholesale customers as well as different pricing.
3. Need zip code lookup to show locations of current galleries.
4. Need registration page to collect customer emails/addresses for net marketing (plume relay).
5. Design should be neutral background since I want to highlight to vivid colors of my work.
6. Site should be easy to navigate.
7. I need to have control of adding content to site as needed (new photos, events, etc.)
8. Need page to list upcoming schedule and event dates.
9. Need all the pages and content from old site, with some revisions to be determined after general design is complete.
...Any suggestions on how to make my site more interesting and functional are welcomed!!
Added photos of newer work today, some of these should appear in high impact areas of the site,. DErek
Question to all...I just remembered that I have already search engine optimized my site using all the appropriate meta tags and photo names, text, etc. for the search terms "glass boxes" and "mosaic mirrors." I am number 1 in zorvik search results of these terms. I need this to not change. Will redesigning my site affect this?
Reason: Hello all, I am in Rome italy right now on business and I have not had time to work with any of you on the designs yet. I am extending the deadline so I can provide more interaction . Derek
Reason: I am still traveling abroad and have no time to work with and review designs. I will be home on the 26th of Oct. then I will be more in touch. Derek
mid to high income women
E-Commerce
- Separate shopping carts for retail and wholesale customers. Wholesale section requires login page.
Lots of pictures of my work. (will supply)
ZIP locator
Broken box repairs page. Customer describes broken piece and can buy replacement part. (size, color, knob color. Can provide pics of all the choices.)
Customer registration page to collect address and email for plume relay or direct mailing.
I like a black or dark gray background of some sort, unless you have a better idea to make my work stand out
- Some kind of link in to social media sites would be great!!!
- keep the layout very simple and easy to navigate. Don't want a confusing page

```html
<!DOCTYPE html>
<html lang="en">
<head>
<meta charset="utf-8">
<title>PebblejarMan – Glass Art</title>
<link href="https://fonts.googleapis.com/css2?family=Montserrat:wght@400;500;700&family=Arimo:wght@400&display=swap" rel="stylesheet">
<style>
:root{
  --page:#222222;
  --page-top:#1b1b1b;
  --footer:#161616;
  --panel-head:#3d3d3d;
  --white:#ffffff;
  --muted:#e6e6e6;
  --field:#7a7a7a;
  --ink:#111111;
  --accent-red:#d81e1e;
}
*{margin:0;padding:0;box-sizing:border-box}
html,body{width:1200px;height:1117px;overflow:hidden}
body{position:relative;background:linear-gradient(#1a1a1a 0,#262626 600px,#262626 953px);font-family:"Montserrat",sans-serif;color:var(--white)}
.abs{position:absolute}

/* header */
.brand-mark{left:44px;top:15px;width:93px;height:105px;background:linear-gradient(135deg,#d9d9d9,#7d7d7d);border-radius:3px}
.brand-name{left:157px;top:34px;font-size:47px;font-weight:700;letter-spacing:1px;color:var(--white);line-height:1}
.util-link{top:70px;font-size:13.5px;display:flex;align-items:center;gap:8px}
.util-link svg{flex:none}

/* navigation */
.main-nav{left:38px;top:130px;width:1117px;height:53px;border-radius:4px;background:linear-gradient(#ffffff,#e2e2e2 55%,#b9b9b9)}
.main-nav a{position:absolute;top:18px;font-family:"Arimo",sans-serif;font-size:15.5px;color:var(--ink);text-decoration:none;white-space:nowrap}
.main-nav .current{left:9px;top:10px;width:83px;height:33px;border-radius:4px;background:linear-gradient(#5c5c5c,#2e2e2e);color:var(--white);text-align:center;line-height:33px;font-family:"Arimo",sans-serif;font-size:15.5px}

/* hero */
.hero{left:40px;top:199px;width:739px;height:420px;border-radius:4px;background:radial-gradient(ellipse at center,#ffffff 40%,#d2d2d2)}
.hero-art{left:95px;top:30px;width:545px;height:370px;border-radius:6px;background:linear-gradient(135deg,#4d8a8a 0%,#3b6fc4 25%,#c8362f 50%,#e2b33d 70%,#a8cc3c 100%)}
.hero-dots{left:663px;top:585px;display:flex;gap:4px}
.hero-dots span{width:14px;height:14px;border-radius:50%;background:#333}
.hero-dots span.on{background:radial-gradient(circle at 40% 35%,#fff,#999)}

.panel-head{height:40px;background:var(--panel-head);border-radius:3px;font-size:19px;padding-left:17px;line-height:40px}

/* products */
.arrow{width:33px;height:33px;border-radius:50%;background:radial-gradient(circle at 45% 35%,#ffffff,#bdbdbd);top:774px}
.product{top:707px;height:180px;background:#000;border-radius:3px;overflow:hidden}
.product .art{height:146px}
.product .caption{height:34px;line-height:34px;text-align:center;font-size:14px}

/* sidebar */
.event{left:868px;display:flex;gap:18px;align-items:flex-start}
.event p{font-size:11.5px;line-height:18px;width:200px;margin-top:7px}
.cal{width:55px;height:62px;flex:none}
.side-text{font-size:11.5px;line-height:18px}
.field{background:var(--field);border-radius:4px;height:28px}
.btn{height:24px;border-radius:3px;background:linear-gradient(#ffffff,#bcbcbc);color:var(--ink);font-size:13px;text-align:center;line-height:24px}
.label{font-size:14px}

/* footer */
.footer{left:0;top:953px;width:1200px;height:164px;background:var(--footer);border-top:2px solid #333}
.footer-text{font-size:14px}
.social{top:1058px;width:26px;height:26px;border-radius:3px}
.shop-promo{left:816px;top:986px;width:334px;height:98px;border-radius:4px;background:linear-gradient(90deg,#e4e4e4,#ffffff 50%,#f0f0f0)}
.shop-art{left:6px;top:8px;width:110px;height:100px;border-radius:4px;background:linear-gradient(135deg,#f05a2a,#c8141c)}
.shop-title{right:16px;top:14px;font-size:24px;color:#222}
.shop-cta{right:17px;top:58px;font-size:18px;color:var(--accent-red)}
</style>
</head>
<body>

<header>
  <div class="abs brand-mark"></div>
  <div class="abs brand-name">PEBBLEJARMAN</div>

  <a class="abs util-link" style="left:693px;top:66px">
    <svg width="26" height="26" viewBox="0 0 26 26"><path d="M1 11 13 3l12 8v2H1z" fill="#ddd"/><rect x="3" y="13" width="20" height="12" fill="#ddd"/><rect x="6" y="16" width="4" height="4" fill="#333"/><rect x="15" y="16" width="5" height="9" fill="#333"/></svg>
    Store Locator
  </a>
  <a class="abs util-link" style="left:861px;top:67px">
    <svg width="30" height="24" viewBox="0 0 30 24"><path d="M2 8c0-6 26-6 26 0v3h-7V7H9v4H2z" fill="#ddd"/><path d="M6 12h18l3 11H3z" fill="#ddd"/><circle cx="15" cy="17" r="3.5" fill="#333"/></svg>
    Contact Us
  </a>
  <a class="abs util-link" style="left:1006px;top:67px">
    <svg width="30" height="26" viewBox="0 0 30 26"><path d="M1 3h5l4 14h14l3-10H8" fill="none" stroke="#ddd" stroke-width="2.5"/><circle cx="11" cy="22" r="2.5" fill="#ddd"/><circle cx="23" cy="22" r="2.5" fill="#ddd"/></svg>
    Shopping Cart
  </a>
</header>

<nav class="abs main-nav">
  <a class="current">Home</a>
  <a style="left:105px">About the Artist</a>
  <a style="left:237px">Glass Boxes</a>
  <a style="left:355px">Mosaic Mirrors</a>
  <a style="left:483px">Mosaic Tables</a>
  <a style="left:609px">Other Photos</a>
  <a style="left:734px">Store Locator</a>
  <a style="left:853px">Shop Online</a>
  <a style="left:970px">Show Schedule</a>
</nav>

<main>
  <section class="abs hero">
    <div class="abs hero-art" role="img" aria-label="Photograph of a glass chest with eight colourful patterned drawers and iridescent knobs"></div>
  </section>
  <div class="abs hero-dots"><span class="on"></span><span></span><span></span><span></span><span></span></div>

  <h2 class="abs panel-head" style="left:43px;top:644px;width:736px;font-weight:400">Featured Products</h2>

  <div class="abs arrow" style="left:42px">
    <svg width="33" height="33" viewBox="0 0 33 33"><path d="M19 10l-6 6.5 6 6.5" fill="none" stroke="#222" stroke-width="3"/></svg>
  </div>
  <div class="abs arrow" style="left:758px">
    <svg width="33" height="33" viewBox="0 0 33 33"><path d="M14 10l6 6.5-6 6.5" fill="none" stroke="#222" stroke-width="3"/></svg>
  </div>

  <article class="abs product" style="left:84px;width:215px">
    <div class="art" role="img" aria-label="Photograph of three patterned glass boxes on tall legs" style="background:linear-gradient(135deg,#5a2b3a,#4a63b8 40%,#c9b04a 70%,#9dc06a)"></div>
    <div class="caption">Click for Glass Boxes</div>
  </article>
  <article class="abs product" style="left:309px;width:213px">
    <div class="art" role="img" aria-label="Photograph of a stacked glass box tower with bright drawers" style="background:linear-gradient(160deg,#1c2a4a,#4c8ab4 45%,#d5582d 75%,#2d56b0)"></div>
    <div class="caption">Click for Glass Boxes</div>
  </article>
  <article class="abs product" style="left:532px;width:213px">
    <div class="art" role="img" aria-label="Photograph of a stacked glass box tower with bright drawers" style="background:linear-gradient(160deg,#1c2a4a,#4c8ab4 45%,#d5582d 75%,#2d56b0)"></div>
    <div class="caption">Click for Glass Boxes</div>
  </article>
</main>

<aside>
  <h2 class="abs panel-head" style="left:844px;top:199px;width:310px;font-weight:400">Upcoming Events</h2>

  <div class="abs event" style="top:257px">
    <svg class="cal" viewBox="0 0 55 62"><rect x="1" y="4" width="53" height="57" rx="4" fill="#f4f4f4"/><rect x="1" y="4" width="53" height="18" rx="4" fill="#2a8fd1"/><text x="6" y="18" font-size="10" fill="#fff" font-family="Arimo,sans-serif">SEP</text><text x="27" y="54" font-size="30" font-weight="700" text-anchor="middle" fill="#222" font-family="Arimo,sans-serif">12</text></svg>
    <p>Lorem ipsum dolor sit amet, consectetur adipisicing elit, sed do eiusmod tempor ....</p>
  </div>
  <div class="abs event" style="top:336px">
    <svg class="cal" viewBox="0 0 55 62"><rect x="1" y="4" width="53" height="57" rx="4" fill="#f4f4f4"/><rect x="1" y="4" width="53" height="18" rx="4" fill="#2a8fd1"/><text x="6" y="18" font-size="10" fill="#fff" font-family="Arimo,sans-serif">SEP</text><text x="27" y="54" font-size="30" font-weight="700" text-anchor="middle" fill="#222" font-family="Arimo,sans-serif">12</text></svg>
    <p>Lorem ipsum dolor sit amet, consectetur adipisicing elit, sed do eiusmod tempor ....</p>
  </div>
  <div class="abs event" style="top:418px">
    <svg class="cal" viewBox="0 0 55 62"><rect x="1" y="4" width="53" height="57" rx="4" fill="#f4f4f4"/><rect x="1" y="4" width="53" height="18" rx="4" fill="#2a8fd1"/><text x="6" y="18" font-size="10" fill="#fff" font-family="Arimo,sans-serif">SEP</text><text x="27" y="54" font-size="30" font-weight="700" text-anchor="middle" fill="#222" font-family="Arimo,sans-serif">12</text></svg>
    <p>Lorem ipsum dolor sit amet, consectetur adipisicing elit, sed do eiusmod tempor ....</p>
  </div>

  <h2 class="abs panel-head" style="left:844px;top:522px;width:310px;font-weight:400">Newsletter</h2>
  <p class="abs side-text" style="left:861px;top:568px;width:285px">Lorem ipsum dolor sit amet, consectetur adipis icing elit, sed do eiusmod tempor ....</p>
  <div class="abs field" style="left:875px;top:614px;width:247px;font-size:14px;line-height:28px;padding-left:12px">Enter Mail ID</div>
  <div class="abs btn" style="left:950px;top:653px;width:102px">SUBSCRIBE</div>

  <h2 class="abs panel-head" style="left:844px;top:709px;width:310px;font-weight:400">Quick User Registration</h2>
  <span class="abs label" style="left:863px;top:770px">User Name :</span>
  <div class="abs field" style="left:970px;top:765px;width:177px"></div>
  <span class="abs label" style="left:863px;top:810px">Password&nbsp; :</span>
  <div class="abs field" style="left:970px;top:805px;width:177px"></div>
  <div class="abs btn" style="left:971px;top:849px;width:85px">SIGN UP</div>
</aside>

<footer class="abs footer"></footer>
<p class="abs footer-text" style="left:56px;top:984px">All Copyrights Reserved&nbsp; @ Pebblejar Man.com</p>
<p class="abs footer-text" style="left:56px;top:1016px">Terms and Conditions |&nbsp; Privacy Policy&nbsp; |&nbsp; Sitemap</p>
<span class="abs social" style="left:61px;background:#3b5a9a"></span>
<span class="abs social" style="left:94px;background:#39a7d8"></span>
<span class="abs social" style="left:127px;background:#1a79b0"></span>
<span class="abs social" style="left:160px;background:#e8701c"></span>

<div class="abs shop-promo">
  <div class="abs shop-art" role="img" aria-label="Illustration of two red shopping bags"></div>
  <div class="abs shop-title">Online Shopping</div>
  <div class="abs shop-cta">Click Here</div>
</div>

</body>
</html>
```